Business Card Design Competition

We need a business card design for our Internet Marketing company. We require both front and back designs and the final card must be 89x53mm in size, plus crop marks to 91x55mm. Colours as per logo, plus perhaps black and/or grey (#828282).
Final text must be editable (if you can supply an editable Fireworks PNG, even better)...
FRONT TEXT:
Full Name
Position
Address Line
Suburb, State, Postcode
Phone: 0000 000 000
Mobile: 0000 000 000
Email: xxx@brimleafpromo.com.au
Web: www.brimleafpromo.com.au
Rear of card should be a fresh design plus our slogan text: "Standing Out Online" in large font, then in small text "Brimleaf Holdings Pty Ltd (ABN: 42 563 701 384)".
Target Market(s)
Small/Medium Businesses
Industry/Entity Type
Business
Look and feel
Each slider illustrates characteristics of the customer's brand and the style your logo design should communicate.

```html
<!DOCTYPE html>
<html lang="en">
<head>
<meta charset="utf-8">
<title>Brimleaf Promo – Business Card</title>
<link href="https://fonts.googleapis.com/css2?family=Source+Sans+3:wght@400;600;700&display=swap" rel="stylesheet">
<style>
  :root {
    --lime: #8cc63f;
    --orange: #f7941d;
    --ink: #1f1f1f;
    --card-black: #1e1e1e;
    --white: #ffffff;
    --mint-light: #f6fbef;
    --mint: #c9e6a4;
    --grey: #828282;
  }
  * { box-sizing: border-box; margin: 0; padding: 0; }
  html, body { width: 1200px; height: 900px; overflow: hidden; background: var(--white); }
  body { position: relative; font-family: "Source Sans 3", "Myriad Pro", sans-serif; }

  .card {
    position: absolute; top: 262px; width: 494px; height: 298px;
    border-radius: 7px; overflow: hidden;
  }

  /* Front */
  .card-front { left: 97px; background: var(--card-black); }
  .front-band-top { position: absolute; left: 0; top: 0; width: 100%; height: 22px; background: var(--lime); }
  .front-band-bottom {
    position: absolute; left: 0; bottom: 0; width: 100%; height: 32px; background: var(--lime);
    color: var(--white); font-size: 13px; text-align: center; line-height: 32px;
  }
  .front-texture {
    position: absolute; left: 217px; top: 22px; width: 277px; height: 244px;
    background: radial-gradient(ellipse at 45% 20%, rgba(90,90,90,.55), rgba(30,30,30,0) 70%);
  }
  .brand-frame {
    position: absolute; left: 0; top: 48px; width: 267px; height: 124px;
    border: 1px solid rgba(255,255,255,.28); border-left: none; border-radius: 0 9px 9px 0;
    background: rgba(255,255,255,.04);
  }
  .brand { position: absolute; display: flex; align-items: center; }
  .brand-dot { border-radius: 50%; background: var(--lime); flex: none; }
  .brand-name { color: var(--lime); font-weight: 600; white-space: nowrap; }
  .card-front .brand { left: 38px; top: 60px; }
  .card-front .brand-dot { width: 44px; height: 44px; margin-right: 9px; }
  .card-front .brand-name { font-size: 24px; }
  .front-slogan { position: absolute; left: 18px; top: 118px; width: 240px; text-align: center; color: var(--white); }
  .front-slogan .slogan { font-size: 25px; font-weight: 700; letter-spacing: -.3px; line-height: 30px; white-space: nowrap; }
  .front-slogan .entity { font-size: 7.5px; font-weight: 700; line-height: 10px; white-space: nowrap; }

  .contact { position: absolute; right: 30px; top: 73px; text-align: right; color: var(--white); }
  .contact .person { color: var(--orange); font-weight: 700; font-size: 19px; line-height: 21px; }
  .contact .address { font-size: 13px; line-height: 16px; margin-top: 12px; }
  .contact-lines { position: absolute; right: 30px; top: 172px; color: var(--white); font-size: 13px; }
  .contact-line { display: flex; justify-content: flex-end; align-items: center; height: 20px; gap: 8px; }
  .contact-line svg { width: 10px; height: 11px; fill: var(--white); flex: none; }
  .accent-bar { position: absolute; right: 0; top: 135px; width: 15px; height: 87px; background: var(--lime); }

  /* Back */
  .card-back {
    left: 628px; border: 1px solid #b9d99a;
    background: linear-gradient(125deg, var(--mint-light) 0%, #e3f2cf 45%, var(--mint) 100%);
  }
  .back-texture {
    position: absolute; right: 0; bottom: 0; width: 260px; height: 190px;
    background: radial-gradient(ellipse at 70% 55%, rgba(255,255,255,.75), rgba(255,255,255,0) 70%);
  }
  .back-tab {
    position: absolute; left: 105px; top: -1px; width: 297px; height: 137px;
    border: 1px solid #9fb58a; border-top: none; border-radius: 0 0 7px 7px;
    background: rgba(255,255,255,.45);
  }
  .card-back .brand { left: 125px; top: 40px; }
  .card-back .brand-dot { width: 56px; height: 56px; margin-right: 10px; }
  .card-back .brand-name { font-size: 30px; }
  .back-slogan { position: absolute; left: 0; top: 160px; width: 100%; text-align: center; color: var(--ink); }
  .back-slogan .slogan { font-size: 42px; font-weight: 700; letter-spacing: -.5px; line-height: 46px; white-space: nowrap; }
  .back-slogan .entity { font-size: 14px; font-weight: 700; line-height: 16px; }
</style>
</head>
<body>
  <section class="card card-front" aria-label="Card front">
    <div class="front-band-top"></div>
    <div class="front-texture" role="img" aria-label="Halftone dot texture"></div>
    <div class="brand-frame"></div>
    <div class="brand"><span class="brand-dot"></span><span class="brand-name">Brimleaf Promo</span></div>
    <div class="front-slogan">
      <p class="slogan">Standing Out Online</p>
      <p class="entity">Brimleaf Holdings Pty Ltd (ABN: 42 563 701 384)</p>
    </div>
    <div class="contact">
      <p class="person">Full Name</p>
      <p class="person">Position</p>
      <p class="address">Address Line<br>Suburb, State, Postcode</p>
    </div>
    <div class="contact-lines">
      <p class="contact-line">0000 000 000
        <svg viewBox="0 0 10 11"><path d="M2 0h2l1 3-1.4 1a6 6 0 0 0 3 3L7.6 5.6l3 1v2.2C8 11 0 5 2 0z"/></svg></p>
      <p class="contact-line">0000 000 000
        <svg viewBox="0 0 10 11"><path d="M2.5 0h5v11h-5zM3.5 1.5v6h3v-6z"/></svg></p>
      <p class="contact-line">xxx@brimleafpromo.com.au
        <svg viewBox="0 0 10 11"><path d="M0 2.5h10v7H0z"/></svg></p>
    </div>
    <div class="accent-bar"></div>
    <div class="front-band-bottom">www.brimleafpromo.com.au</div>
  </section>

  <section class="card card-back" aria-label="Card back">
    <div class="back-texture" role="img" aria-label="Faint halftone dot texture"></div>
    <div class="back-tab"></div>
    <div class="brand"><span class="brand-dot"></span><span class="brand-name">Brimleaf Promo</span></div>
    <div class="back-slogan">
      <p class="slogan">Standing Out Online</p>
      <p class="entity">Brimleaf Holdings Pty Ltd (ABN: 42 563 701 384)</p>
    </div>
  </section>
</body>
</html>
```